Save the Date for 77th birthday fundraiser

We need a design for a Save the Date as we are preparing to celebrate our founder Dell Pembrook’s 77 birthday next year.
We would like a professional illustrated Save the Date with the theme “How it started, How it’s going”. Attached is a picture from the early 70’s and another one from yesterday. We want him to look his absolute best.
We need the date, location, and contact details to RSVP incorporated into the design:
April 9
Marlow Ainsley Hall, Austin Texas
team@guidewellpath.com
AND PLEASE REMEMBER THIS IS A SURPRISE!
We would also like to include elements that evoke what he does: Author (he’s published 2 books), Speaker (a microphone), Business Coach, and Entrepreneur.
Feelings we would like to evoke when people see the image: Would like people to think we are a professional company that is throwing a fun event for all the clients and friends Dell has made along his extraordinary 50-year career.
Thank you so much!

```html
<!DOCTYPE html>
<html lang="en">
<head>
<meta charset="utf-8">
<title>Save the Date – Dell Pembrook</title>
<link rel="stylesheet" href="https://fonts.googleapis.com/css2?family=Dancing+Script:wght@700&family=Poppins:wght@300;400;600;800&display=block">
<style>
  :root {
    --stage: #cad2da;
    --navy: #2b2c6a;
    --navy-deep: #23245a;
    --frame: #cdd6db;
    --teal: #3aabb5;
    --ink-light: #e4e8ee;
    --ghost: rgba(255, 255, 255, 0.07);
    --script: "Dancing Script", "Brush Script MT", cursive;
  }
  html, body {
    margin: 0;
    width: 993px;
    height: 1200px;
    overflow: hidden;
    background: var(--stage);
  }
  .card {
    position: absolute;
    left: 183px;
    top: 161px;
    width: 627px;
    height: 877px;
    background: var(--navy);
    overflow: hidden;
    font-family: "Poppins", sans-serif;
  }
  .ghost-names {
    position: absolute;
    inset: 0;
    font-family: var(--script);
    font-weight: 700;
    font-size: 104px;
    line-height: 122px;
    color: var(--ghost);
    white-space: nowrap;
    margin-top: -22px;
    margin-left: 8px;
  }
  .ghost-names span { display: block; }
  .polaroid {
    position: absolute;
    left: 61px;
    top: 75px;
    width: 506px;
    height: 622px;
    background: var(--frame);
    transform: rotate(-3deg);
    box-shadow: 0 14px 22px rgba(10, 10, 40, 0.55);
    text-align: center;
    color: var(--navy);
  }
  .photo {
    position: absolute;
    left: 17px;
    top: 17px;
    width: 472px;
    height: 405px;
    background: linear-gradient(135deg, #e9e9e9 0%, #c9c4bc 45%, #6e6a65 100%);
    box-shadow: inset 0 6px 14px rgba(0, 0, 0, 0.25);
  }
  .intro {
    position: absolute;
    left: 0;
    right: 0;
    top: 462px;
    font-weight: 300;
    font-size: 21px;
    letter-spacing: 4px;
    line-height: 30px;
    margin: 0;
  }
  .name {
    position: absolute;
    left: 0;
    right: 0;
    top: 524px;
    margin: 0;
    font-family: var(--script);
    font-weight: 700;
    font-size: 52px;
    line-height: 56px;
  }
  .tagline {
    position: absolute;
    left: 0;
    right: 0;
    top: 582px;
    margin: 0;
    padding-left: 11px;
    font-weight: 600;
    font-size: 14px;
    letter-spacing: 11px;
  }
  .badge {
    position: absolute;
    left: 397px;
    top: 665px;
    width: 162px;
    height: 162px;
    border-radius: 50%;
    background: var(--navy-deep);
    border: 2px solid var(--teal);
    box-sizing: border-box;
    box-shadow: 0 10px 18px rgba(10, 10, 40, 0.55);
    transform: rotate(-10deg);
    font-family: "Poppins", sans-serif;
    color: #fff;
  }
  .badge .save, .badge .date {
    position: absolute;
    font-weight: 800;
    font-size: 40px;
    line-height: 1;
    background: linear-gradient(90deg, #ffffff 20%, var(--teal) 100%);
    -webkit-background-clip: text;
    background-clip: text;
    color: transparent;
  }
  .badge .save { left: 22px; top: 28px; }
  .badge .the { position: absolute; left: 60px; top: 64px; font-weight: 300; font-size: 24px; line-height: 1; }
  .badge .date { left: 30px; top: 86px; }
  .badge .day { position: absolute; left: 62px; top: 124px; font-weight: 600; font-size: 15px; line-height: 1; }
  .rsvp {
    position: absolute;
    left: 77px;
    top: 756px;
    color: var(--ink-light);
    font-size: 16.5px;
    line-height: 21px;
    margin: 0;
  }
  .rsvp .label {
    display: block;
    font-weight: 300;
    letter-spacing: 4px;
    font-size: 17px;
    margin-bottom: 3px;
  }
</style>
</head>
<body>
  <main class="card">
    <div class="ghost-names" aria-hidden="true">
      <span>Dell Pembrook</span>
      <span>Dell Pembrook</span>
      <span>Dell Pembrook</span>
      <span>Dell Pembrook</span>
      <span>Dell Pembrook</span>
      <span>Dell Pembrook</span>
      <span>Dell Pembrook</span>
    </div>

    <section class="polaroid">
      <div class="photo" role="img" aria-label="Cut-out photos of the founder in a top hat and vest, one from the early 1970s and one from today, over icons for author, speaker, coach and entrepreneur"></div>
      <p class="intro">CELEBRATING EXTRAORDINARY<br>50 YEARS OF</p>
      <h1 class="name">Dell Pembrook</h1>
      <p class="tagline">GUIDE WELL PATH</p>
    </section>

    <div class="badge" aria-label="Save the Date, April 9">
      <span class="save">Save</span>
      <span class="the">the</span>
      <span class="date">Date</span>
      <span class="day">April 9</span>
    </div>

    <p class="rsvp">
      <span class="label">RSVP</span>
      Marlow Ainsley Hall,<br>
      Austin Texas<br>
      team@guidewellpath.com
    </p>
  </main>
</body>
</html>
```